Dale Morrikan Plumbing and Heating

Need a card design for a plumbing and heating company that does service and repair, remodels, and plumbing in new construction. Please add following on back side of card; Boilers, Water heaters, Gas lines, Sump pumps, Toilet repairs, Faucet repairs, Pipe thawing, Radiant heating, New construction, Remodels.

Industry/Entity Type

Plumber

Contact Information for Business Card

Was thinking white gloss card with colored logo in middle or black glossy card with silver logo in middle. Just a thought but very open to other designs.

Requirements
Must have
• Need following on front of card;
• P(203) 321-8689
• C(203) 232-9069
• Dale Morrikan 275 Larkwell St West, Stamford, Ct 06214
• service@DrainHearth.example (plumbing in blue, heating in red)
• www.DrainHearth.example (plumbing in blue, heating in red)
• Fully Licensed and Insured
Nice to have
• Elegant design

```html
<!DOCTYPE html>
<html lang="en">
<head>
<meta charset="utf-8">
<title>Dale Morrikan Plumbing and Heating – Business Card</title>
<link rel="stylesheet" href="https://fonts.googleapis.com/css2?family=Open+Sans:wght@400;600;700&family=Michroma&display=swap">
<style>
  :root {
    --bg: #d9d9d9;
    --card: #ffffff;
    --blue: #1d5fb4;
    --blue-deep: #0f3f8c;
    --blue-light: #3b8de0;
    --red: #d2232a;
    --grey: #666a70;
    --ink: #55595e;
  }
  * { box-sizing: border-box; margin: 0; padding: 0; }
  html, body { width: 1200px; height: 852px; overflow: hidden; }
  body {
    background: var(--bg);
    font-family: "Open Sans", Arial, sans-serif;
    position: relative;
  }
  .card {
    position: absolute;
    width: 540px;
    height: 308px;
    background: var(--card);
    border-radius: 22px;
    overflow: hidden;
    box-shadow: 0 10px 24px rgba(0,0,0,.22);
  }
  .card--back { left: 80px; top: 110px; }
  .card--front { left: 600px; top: 440px; }

  .brand {
    display: flex;
    align-items: center;
    gap: 10px;
    color: var(--blue);
    font-weight: 700;
    text-transform: uppercase;
    letter-spacing: .5px;
  }
  .brand__dot {
    width: 30px; height: 30px; border-radius: 50%;
    background: var(--blue);
    flex: none;
  }
  .brand__name { line-height: 1.1; }

  /* back side */
  .card--back .brand {
    position: absolute; left: 0; right: 0; top: 40px;
    justify-content: center; font-size: 22px;
  }
  .services {
    position: absolute; left: 0; right: 0; top: 112px; height: 112px;
    padding: 0 28px;
    background: linear-gradient(90deg, var(--blue-deep), var(--blue) 55%, var(--blue-light));
    color: #fff;
    display: flex; flex-direction: column; justify-content: center; align-items: center;
    gap: 8px;
    font-family: "Michroma", "Open Sans", sans-serif;
    font-size: 11px; letter-spacing: .3px; text-transform: uppercase;
    text-align: center;
  }
  .services p { white-space: nowrap; line-height: 1.2; }
  .site-line {
    position: absolute; left: 0; right: 0; top: 248px;
    display: flex; align-items: center; justify-content: center; gap: 14px;
    font-size: 14px; font-weight: 600; color: var(--ink);
  }
  .site-line::before, .site-line::after {
    content: ""; width: 70px; height: 1px; background: #aaa;
  }
  .blue { color: var(--blue); }
  .red { color: var(--red); }

  /* front side */
  .edge {
    position: absolute; left: 0; top: 0; bottom: 0; width: 54px;
    background: linear-gradient(180deg, var(--blue-light), var(--blue-deep));
    border-right: 4px solid var(--red);
  }
  .card--front .brand {
    position: absolute; left: 86px; top: 34px; font-size: 21px;
  }
  .person { position: absolute; left: 86px; top: 118px; }
  .person__name { font-size: 20px; font-weight: 600; color: var(--blue); }
  .person__title { font-size: 11px; color: var(--ink); margin-top: -2px; }
  .contacts {
    position: absolute; left: 86px; top: 172px;
    list-style: none; font-size: 13px; color: var(--ink);
  }
  .contacts li { display: flex; align-items: center; gap: 10px; height: 21px; }
  .contacts svg { width: 14px; height: 14px; fill: var(--blue); flex: none; }
  .contacts .no-icon { padding-left: 24px; }
  .licensed {
    position: absolute; right: 30px; top: 118px;
    text-align: right; font-size: 13px; color: var(--blue); line-height: 1.35;
  }
</style>
</head>
<body>

<section class="card card--back" aria-label="Card back">
  <div class="brand">
    <span class="brand__dot"></span>
    <span class="brand__name">Dale Morrikan<br>Plumbing and Heating</span>
  </div>
  <div class="services">
    <p>Boilers • Water Heaters • Gas Lines • Sump Pumps</p>
    <p>Toilet Repairs • Faucet Repairs • Pipe Thawing</p>
    <p>Radiant Heating • New Construction • Remodels</p>
  </div>
  <p class="site-line"><span>www.<span class="blue">Drain</span><span class="red">Hearth</span>.example</span></p>
</section>

<section class="card card--front" aria-label="Card front">
  <div class="edge"></div>
  <div class="brand">
    <span class="brand__dot"></span>
    <span class="brand__name">Dale Morrikan<br>Plumbing and Heating</span>
  </div>
  <div class="person">
    <p class="person__name">Dale Morrikan</p>
    <p class="person__title">Director</p>
  </div>
  <ul class="contacts">
    <li><svg viewBox="0 0 16 16"><path d="M3 1h3l1.5 4-2 1.2a9 9 0 0 0 4.3 4.3L11 8.5l4 1.5v3a2 2 0 0 1-2 2A12 12 0 0 1 1 3a2 2 0 0 1 2-2z"/></svg><span>(203) 555-0147</span></li>
    <li><svg viewBox="0 0 16 16"><path d="M4 1h8v4H4zM2 6h12a1 1 0 0 1 1 1v5h-3v3H4v-3H1V7a1 1 0 0 1 1-1zm3 5v3h6v-3z"/></svg><span>(203) 555-0183</span></li>
    <li><svg viewBox="0 0 16 16"><path d="M8 1a7 7 0 1 0 0 14A7 7 0 0 0 8 1zm0 1.5c.8 0 1.8 1.5 2.1 4H5.9C6.2 4 7.2 2.5 8 2.5zM2.6 7.5h2A11 11 0 0 0 5 11H3.3a5.5 5.5 0 0 1-.7-3.5zm8.8 0h2a5.5 5.5 0 0 1-.7 3.5H11a11 11 0 0 0 .4-3.5zm-5.5 0h4.2a9 9 0 0 1-.5 3.5H6.4a9 9 0 0 1-.5-3.5z"/></svg><span><span class="blue">Drain</span><span class="red">Hearth</span>.example</span></li>
    <li><svg viewBox="0 0 16 16"><path d="M1 3h14v10H1zm1.5 1.5v.4L8 9l5.5-4.1v-.4z"/></svg><span>service@<span class="blue">Drain</span><span class="red">Hearth</span>.example</span></li>
    <li class="no-icon"><span>275 Larkwell St West, Stamford, CT 06214</span></li>
  </ul>
  <p class="licensed">Fully Licensed<br>and Insured</p>
</section>

</body>
</html>
```